Toward Bright Morrow (TWBM) Business Card - company with a mission

Note* The file attached... orange with "Toward Bright MORROW" (in CAPS) is our logo. I am also open to having the text "toward bright morrow" OUTSIDE the orange round logo for business card (so yes, you may take the text out).

The info: (the following info are separate. So either you can use Martin or Helena for now, but that will be 2 separate cards, not together in one card. Thanks!!

Martin K Pardo
202.555.0183
martin@towardbrightmorrow.example
Managing Partner

Helena R Voss
202.555.0147
helena@towardbrightmorrow.example
Managing Partner

Our website: www.towardbrightmorrow.example

TWBM LLC stands for Toward Bright Morrow (non profit arm is called dawn lift foundation)—our business is based out of New York City and has a non-profit arm where for every bar of soap you purchase, we donate a bar (don’t want any designs that limits us to only soap). Currently working with South Africa. We want the focus to be organic/natural soap with a mission.

Looking for a clean, fresh design.

Industry/Entity Type

Non-Profit

Requirements
Must have
• Clean, fresh, refreshing. Design should not be too busy.

```html
<!DOCTYPE html>
<html lang="en">
<head>
<meta charset="utf-8">
<title>Toward Bright Morrow — Business Card</title>
<link href="https://fonts.googleapis.com/css2?family=Jost:wght@400;500&display=swap" rel="stylesheet">
<style>
  :root {
    --backdrop: #efe9e2;
    --card-white: #ffffff;
    --orange: #f5ad6e;
    --orange-light: #f7bb86;
    --text-light: #ffffff;
  }
  html, body {
    margin: 0;
    width: 1200px;
    height: 1000px;
    overflow: hidden;
    background: var(--backdrop);
    font-family: "Jost", "Futura", sans-serif;
  }
  .canvas { position: relative; width: 1200px; height: 1000px; }
  .card {
    position: absolute;
    top: 150px;
    width: 457px;
    height: 743px;
    border-radius: 30px;
    overflow: hidden;
  }
  .card-front { left: 143px; background: var(--card-white); }
  .card-back { left: 600px; background: var(--orange); }

  .front-band {
    position: absolute;
    left: 90px;
    width: 282px;
    top: 0;
    bottom: 0;
    background: var(--orange);
  }
  .brand-mark {
    position: absolute;
    left: 64px;
    top: 92px;
    width: 330px;
    height: 330px;
    box-sizing: border-box;
    border: 6px solid var(--text-light);
    border-radius: 50%;
    background: var(--orange);
    display: flex;
    align-items: center;
    justify-content: center;
    color: var(--text-light);
    font-weight: 500;
    font-size: 82px;
    letter-spacing: 2px;
  }
  .brand-name {
    position: absolute;
    left: 80px;
    width: 302px;
    top: 466px;
    margin: 0;
    text-align: center;
    color: var(--text-light);
    font-weight: 400;
    line-height: 1;
  }
  .brand-name .line-small { display: block; font-size: 36px; margin-bottom: 12px; }
  .brand-name .line-large { display: block; font-size: 54px; margin-top: 14px; }
  .website {
    position: absolute;
    left: 80px;
    width: 302px;
    top: 694px;
    text-align: center;
    color: var(--text-light);
    font-size: 16px;
  }

  .back-pattern {
    position: absolute;
    inset: 0;
    background: radial-gradient(circle at 60% 45%, var(--orange-light) 0%, var(--orange) 70%);
  }
  .person {
    position: absolute;
    left: 0;
    right: 0;
    top: 140px;
    text-align: center;
    color: var(--text-light);
    line-height: 1.25;
  }
  .person-name { margin: 0; font-size: 32px; font-weight: 400; letter-spacing: 1px; }
  .person-role { margin: 2px 0 0; font-size: 28px; font-weight: 400; letter-spacing: 0.5px; }
  .contact {
    position: absolute;
    left: 0;
    right: 0;
    top: 611px;
    text-align: center;
    color: var(--text-light);
    font-size: 22px;
    list-style: none;
    margin: 0;
    padding: 0;
  }
  .contact li { display: flex; align-items: center; justify-content: center; gap: 6px; margin-bottom: 24px; }
  .contact svg { width: 24px; height: 24px; }
</style>
</head>
<body>
<main class="canvas">
  <section class="card card-front" aria-label="Card front">
    <div class="front-band"></div>
    <div class="brand-mark">TWBM</div>
    <h1 class="brand-name">
      <span class="line-small">TOWARD</span>
      <span class="line-small">BRIGHT</span>
      <span class="line-large">MORROW</span>
    </h1>
    <div class="website">www.towardbrightmorrow.example</div>
  </section>

  <section class="card card-back" aria-label="Card back">
    <div class="back-pattern" role="img" aria-label="Soft decorative background pattern in light orange tones"></div>
    <div class="person">
      <h2 class="person-name">MARTIN K PARDO</h2>
      <p class="person-role">Managing Partner</p>
    </div>
    <ul class="contact">
      <li>
        <svg viewBox="0 0 24 24" aria-hidden="true">
          <circle cx="12" cy="12" r="11" fill="var(--text-light)"/>
          <rect x="8" y="5" width="8" height="14" rx="1.5" fill="var(--orange)"/>
          <rect x="9.5" y="7" width="5" height="6" fill="var(--text-light)"/>
        </svg>
        202.555.0183
      </li>
      <li>
        <svg viewBox="0 0 24 24" aria-hidden="true">
          <circle cx="12" cy="12" r="11" fill="var(--text-light)"/>
          <rect x="6" y="8" width="12" height="8" rx="1" fill="var(--orange)"/>
          <path d="M6 8 L12 13 L18 8" fill="none" stroke="var(--text-light)" stroke-width="1.2"/>
        </svg>
        martin@towardbrightmorrow.example
      </li>
    </ul>
  </section>
</main>
</body>
</html>
```